Refresh of The Marston Collective business card

Update business card design using existing primary logo. Names, numbers, etc. are too hard to read on current design.

Target Market(s)

We are a CPA firm.

Industry/Entity Type

Accountant

Contact Information for Business Card

update current card

Colors
0355a3
3176b5
85acd3
0792cd

Requirements
Must have
• Easier to read phone numbers and names
• Use existing logo
Nice to have
• We love our color scheme and current TMC logo. But the names and phone numbers are too small and card just look old and stale.

```html
<!DOCTYPE html>
<html lang="en">
<head>
<meta charset="utf-8">
<title>The Marston Collective – Business Card</title>
<link rel="stylesheet" href="https://fonts.googleapis.com/css2?family=Cinzel:wght@500&family=Roboto:wght@400&display=swap">
<style>
  :root {
    --navy: #0355a3;
    --navy-deep: #1c3f7c;
    --navy-edge: #1a3566;
    --blue-mid: #3176b5;
    --blue-light: #85acd3;
    --ink: #4a4a4a;
    --paper: #ffffff;
    --ghost: #eef0f5;
    --ghost-line: #e2e5ec;
    --stage: #d9dadc;
  }
  * { margin: 0; padding: 0; box-sizing: border-box; }
  html, body { width: 1200px; height: 1000px; overflow: hidden; }
  body { background: var(--stage); position: relative; font-family: "Roboto", Arial, sans-serif; }

  .card {
    position: absolute; left: 220px; width: 760px; border-radius: 28px; overflow: hidden;
  }
  .card--front {
    top: 50px; height: 434px;
    background: radial-gradient(ellipse at 55% 40%, var(--blue-mid) 0%, var(--navy) 40%, var(--navy-deep) 75%, var(--navy-edge) 100%);
  }
  .card--back { top: 524px; height: 436px; background: var(--paper); }

  .brand { position: absolute; display: flex; align-items: center; }
  .brand__disc { border-radius: 50%; flex: none; }
  .brand__name { font-family: "Cinzel", Georgia, serif; font-weight: 500; line-height: 1.05; letter-spacing: 1px; }

  .card--front .brand { left: 193px; top: 153px; }
  .card--front .brand__disc { width: 112px; height: 112px; border: 4px solid var(--paper); margin-right: 28px; }
  .card--front .brand__name { color: var(--paper); font-size: 38px; }

  .front__web { position: absolute; left: 0; right: 0; top: 370px; text-align: center; color: var(--paper); font-size: 17px; }

  .ghost-disc {
    position: absolute; left: 500px; top: 160px; width: 300px; height: 300px; border-radius: 50%;
    background: var(--ghost); border: 6px solid var(--ghost-line);
  }

  .card--back .brand { left: 448px; top: 42px; }
  .card--back .brand__disc { width: 90px; height: 90px; background: var(--navy); border: 3px solid #333; margin-right: 12px; }
  .card--back .brand__name { color: var(--navy); font-size: 25px; }

  .holder { position: absolute; left: 50px; top: 170px; font-family: "Cinzel", Georgia, serif; font-weight: 500; font-size: 24px; color: var(--navy); letter-spacing: 0.5px; }
  .address { position: absolute; left: 49px; top: 218px; font-size: 18px; line-height: 23px; color: var(--ink); }
  .contacts { position: absolute; left: 48px; top: 277px; list-style: none; font-size: 17.5px; line-height: 24.2px; color: var(--ink); }
  .contacts li { display: flex; align-items: center; }
  .contacts svg { width: 13px; height: 13px; margin-right: 6px; fill: var(--navy); flex: none; }
</style>
</head>
<body>
  <section class="card card--front">
    <div class="brand">
      <div class="brand__disc"></div>
      <div class="brand__name">The Marston<br>Collective</div>
    </div>
    <p class="front__web">www.marstoncollective.com</p>
  </section>

  <section class="card card--back">
    <div class="ghost-disc"></div>
    <div class="brand">
      <div class="brand__disc"></div>
      <div class="brand__name">The Marston<br>Collective</div>
    </div>
    <h1 class="holder">Daniel R. Marston, CPA</h1>
    <p class="address">318 W. Larkspur Ave. Suite 104<br>Winter Park, Florida 32789</p>
    <ul class="contacts">
      <li><svg viewBox="0 0 16 16" aria-hidden="true"><path d="M3.5 1l2.5 3-1.5 2c1 2 3 4 5 5l2-1.5 3 2.5-1.5 2.5C7 15 1 9 1 2.5z"/></svg>555.201.4837</li>
      <li><svg viewBox="0 0 16 16" aria-hidden="true"><path d="M4 0h8v16H4zM5.5 2v10h5V2zM7 13.2h2v1.3H7z" fill-rule="evenodd"/></svg>555.318.2096</li>
      <li><svg viewBox="0 0 16 16" aria-hidden="true"><path d="M4 1h8v4H4zM1 6h14v7h-3v2H4v-2H1zM5 10v4h6v-4z" fill-rule="evenodd"/></svg>555.472.9150</li>
      <li><svg viewBox="0 0 16 16" aria-hidden="true"><path d="M1 3h14v10H1zM2 4l6 5 6-5z" fill-rule="evenodd"/></svg>dan@marstoncollective.com</li>
      <li><svg viewBox="0 0 16 16" aria-hidden="true"><path d="M8 1a7 7 0 110 14A7 7 0 018 1zm0 1.5a5.5 5.5 0 100 11 5.5 5.5 0 000-11zM2.5 7.3h11v1.4h-11zM7.3 2.5h1.4v11H7.3z" fill-rule="evenodd"/></svg>www.marstoncollective.com</li>
    </ul>
  </section>
</body>
</html>
```